Energy trading company (Voltarix) needs a business card

We need a business card for a company based in Central America. Our main purpose is trading energy . We already have the logo but we need some good creativity to design a high impact business card. Colors blue, orange, green can be used or we would like to see good combinatios with our logo

Target Market(s)

Energy

Industry/Entity Type

Power Generation

Contact Information for Business Card

Logo , headquarters , name, background

Font styles to use
Serif
Sans Serif

Colors

Designer to choose colors to be used in the design.

Requirements
Must have
• it must have a fresh and clean view
Nice to have
• good backgrounds that combine with the logo
Should not have
• too much words

```html
<!DOCTYPE html>
<html lang="en">
<head>
<meta charset="utf-8">
<title>Voltarix Business Card</title>
<link href="https://fonts.googleapis.com/css2?family=Montserrat:wght@500&family=Oswald:wght@500;600&family=Roboto:wght@400&display=swap" rel="stylesheet">
<style>
  :root {
    --stage: #26272b;
    --card: #1e2022;
    --card-edge: #2a2c2f;
    --accent: #f39322;
    --ink-light: #f2f2f2;
    --ink-soft: #cfd0d2;
    --rule: #6b6d70;
  }
  * { box-sizing: border-box; margin: 0; padding: 0; }
  html, body {
    width: 1200px;
    height: 800px;
    overflow: hidden;
    background: var(--stage);
  }
  .canvas {
    position: relative;
    width: 1200px;
    height: 800px;
    background: var(--stage);
  }
  .card {
    position: absolute;
    width: 520px;
    height: 300px;
    background: var(--card);
    border: 1px solid var(--card-edge);
    border-radius: 3px;
    box-shadow: 0 18px 40px rgba(0,0,0,.45);
  }
  .card--front { left: 70px; top: 110px; }
  .card--back { left: 610px; top: 390px; }

  /* Front */
  .brand {
    position: absolute;
    inset: 0;
    display: flex;
    align-items: center;
    justify-content: center;
    gap: 16px;
  }
  .brand__dot {
    width: 34px;
    height: 34px;
    border-radius: 50%;
    background: var(--accent);
  }
  .brand__name {
    font-family: "Montserrat", sans-serif;
    font-weight: 500;
    font-size: 46px;
    letter-spacing: 2px;
    color: var(--accent);
    text-transform: uppercase;
  }

  /* Back */
  .person {
    position: absolute;
    left: 40px;
    top: 92px;
    width: 200px;
    text-align: right;
  }
  .person__name {
    font-family: "Oswald", sans-serif;
    font-weight: 600;
    font-size: 30px;
    line-height: 1;
    color: var(--ink-light);
    text-transform: uppercase;
  }
  .person__role {
    font-family: "Oswald", sans-serif;
    font-weight: 500;
    font-size: 15px;
    letter-spacing: .5px;
    margin-top: 5px;
    color: var(--accent);
    text-transform: uppercase;
  }
  .divider {
    position: absolute;
    left: 258px;
    top: 72px;
    width: 1px;
    height: 92px;
    background: var(--rule);
  }
  .contacts {
    position: absolute;
    left: 276px;
    top: 86px;
    list-style: none;
    font-family: "Roboto", sans-serif;
    font-size: 13px;
    color: var(--ink-soft);
  }
  .contacts li {
    display: flex;
    align-items: center;
    gap: 8px;
    height: 22px;
  }
  .contacts svg { width: 12px; height: 12px; fill: var(--accent); flex: none; }
  .contacts .accent { color: var(--accent); }
  .address {
    position: absolute;
    left: 40px;
    bottom: 38px;
    display: flex;
    align-items: center;
    gap: 12px;
    font-family: "Roboto", sans-serif;
    font-size: 13px;
    color: var(--ink-soft);
  }
  .address svg { width: 12px; height: 15px; }
</style>
</head>
<body>
<main class="canvas">

  <section class="card card--front" aria-label="Card front">
    <div class="brand">
      <span class="brand__dot"></span>
      <span class="brand__name">Voltarix</span>
    </div>
  </section>

  <section class="card card--back" aria-label="Card back">
    <div class="person">
      <p class="person__name">Marcus Hale</p>
      <p class="person__role">Managing Director</p>
    </div>
    <span class="divider"></span>
    <ul class="contacts">
      <li>
        <svg viewBox="0 0 24 24"><path d="M6.6 10.8a15.1 15.1 0 0 0 6.6 6.6l2.2-2.2c.3-.3.7-.4 1-.2 1.1.4 2.3.6 3.6.6.6 0 1 .4 1 1V20c0 .6-.4 1-1 1A17 17 0 0 1 3 4c0-.6.4-1 1-1h3.5c.6 0 1 .4 1 1 0 1.3.2 2.5.6 3.6.1.3 0 .7-.2 1z"/></svg>
        (507) 418-2297
      </li>
      <li>
        <svg viewBox="0 0 24 24"><path d="M2 5h20v14H2z M2 5l10 8 10-8" fill="none" stroke="#f39322" stroke-width="2.5"/></svg>
        info@voltarixmail.com
      </li>
      <li>
        <svg viewBox="0 0 24 24"><circle cx="12" cy="12" r="10"/><path d="M2 12h20M12 2c3 3 3 17 0 20M12 2c-3 3-3 17 0 20" stroke="#1e2022" stroke-width="1.6" fill="none"/></svg>
        <span>www.<span class="accent">voltarixweb</span>.com</span>
      </li>
    </ul>
    <p class="address">
      <svg viewBox="0 0 12 15"><path d="M6 1a5 5 0 0 0-5 5c0 3.5 5 8 5 8s5-4.5 5-8a5 5 0 0 0-5-5z" fill="none" stroke="#f39322" stroke-width="1.6"/><circle cx="6" cy="6" r="1.6" fill="#f39322"/></svg>
      PO BOX 48, Calle Norte, 5th avenue, Port Alder
    </p>
  </section>

</main>
</body>
</html>
```